business card for law firm that reflects the web site -www.MarlaQuentby.com. That is pleasant to read

We need a business card for a small law firm. Your company designed our logo - tree of life - which I can provide to the designers. The card should be on both sides. Use the coloring from the web site (www.MarlaQuentby.com) and logo (I have several formats). I am attaching the logo, but not sure what format to use.

First side name of firm: Law Office of M.K. Quentby, P.A. 4819 West Pallisor, Suite 300, Ardenvale, AZ 80000, Phone: 555.010.3841, Fax: 555.010.7290, web site: www.MarlaQuentby.com, email: MQuentby@MarlaQuentby.com.
Marla K. Quentby Bankruptcy and Foreclosure Attorney & Counselor.
Back side (perhaps vertical) the logo and then Notes with lines. At the bottom: Proud to help people and small businesses file for bankruptcy protection. We are a debt relief agency.
Updates

I have several versions of the logo. Will be happy to share whatever you need. Added Sunday, April 3, 2016

Target Market(s)

everyone

Industry/Entity Type

Legal

Contact Information for Business Card

I prefer something unique (rounded edges, design that adopts my web site - www.MarlaQuentby.com.

Font styles to use
Serif

Requirements
Must have
• First side name of firm: Law Office of M.K. Quentby, P.A. 4819 West Pallisor, Suite 300, Ardenvale, AZ 80000, Phone: 555.010.3841, Fax: 555.010.7290, web site: www.MarlaQuentby.com, email: MQuentby@MarlaQuentby.com.
• Marla K. Quentby Bankruptcy and Foreclosure Attorney & Counselor.
• Back side (perhaps vertical) the logo and then Notes with lines. At the bottom: Proud to help people and small businesses file for bankruptcy protection. We are a debt relief agency.
• Green and brown colors that reflect the web site: www.MarlaQuentby.com
Should not have
• Type so small that older people cannot read.

```html
<!DOCTYPE html>
<html lang="en">
<head>
<meta charset="utf-8">
<title>M.K. Quentby Business Card</title>
<link rel="stylesheet" href="https://fonts.googleapis.com/css2?family=Jost:wght@400;500&display=swap">
<style>
  :root {
    --backdrop: #ece7df;
    --brown: #3a1a14;
    --tan: #d9c896;
    --ink: #2a1510;
    --paper: #ffffff;
    --forest: #1f5a2c;
  }
  * { box-sizing: border-box; margin: 0; padding: 0; }
  html, body { width: 1200px; height: 799px; overflow: hidden; }
  body {
    background: var(--backdrop);
    font-family: "Jost", "Futura", sans-serif;
    color: var(--ink);
    position: relative;
  }
  .card {
    position: absolute;
    top: 250px;
    width: 520px;
    height: 298px;
    background: var(--paper);
    box-shadow: 0 6px 18px rgba(0,0,0,.18);
    overflow: hidden;
  }
  .card--front { left: 50px; }
  .card--back { left: 630px; }

  /* Front side */
  .front__band {
    position: absolute; left: 0; top: 0; bottom: 0; width: 168px;
    background: var(--brown);
  }
  .front__panel {
    position: absolute; left: 174px; top: 0; right: 0; bottom: 0;
    background: var(--tan);
    border-bottom-right-radius: 80px;
  }
  .front__seal {
    position: absolute; left: 34px; top: 99px;
  }
  .front__details {
    position: absolute; right: 22px; top: 14px;
    text-align: right;
    font-size: 13.5px; line-height: 1.28;
  }
  .front__web { font-size: 11.5px; line-height: 1.3; margin-bottom: 24px; }
  .front__name { margin-bottom: 20px; }
  .front__address { margin-bottom: 18px; }

  /* Back side */
  .back__strip {
    position: absolute; left: 0; top: 0; bottom: 0; width: 160px;
    background: var(--tan);
  }
  .back__field {
    position: absolute; left: 166px; top: 0; right: 0; bottom: 0;
    background: var(--brown);
    border-top-right-radius: 70px;
  }
  .back__message {
    position: absolute; left: 160px; top: 0;
    width: 298px; height: 160px;
    transform-origin: 0 0;
    transform: rotate(90deg);
    padding: 22px 24px;
    font-size: 15px; line-height: 1.25;
  }
  .back__seal {
    position: absolute; left: 215px; top: 20px;
  }
  .seal-name {
    font-family: "Jost", "Futura", sans-serif;
    font-weight: 500;
    fill: var(--paper);
  }
</style>
</head>
<body>

  <section class="card card--front" aria-label="Business card, contact side">
    <div class="front__band"></div>
    <div class="front__panel"></div>
    <svg class="front__seal" width="100" height="100" viewBox="0 0 100 100">
      <circle cx="50" cy="50" r="48" fill="var(--paper)"/>
      <circle cx="50" cy="50" r="44" fill="var(--forest)"/>
      <text class="seal-name" x="50" y="54" text-anchor="middle" font-size="11">M.K. Quentby</text>
    </svg>
    <div class="front__details">
      <p class="front__web">www.MarlaQuentby.com<br>MQuentby@MarlaQuentby.com</p>
      <p class="front__name">Marla K. Quentby Bankruptcy<br>Foreclosure Attorney<br>Counselor.</p>
      <p class="front__address">Law Office of M.K. Quentby,<br>P.A. 4819 West Pallisor,<br>Suite 300, Ardenvale,<br>AZ 80000,</p>
      <p class="front__phone">Phone: 555.010.3841,<br>Fax: 555.010.7290,</p>
    </div>
  </section>

  <section class="card card--back" aria-label="Business card, message side">
    <div class="back__strip"></div>
    <div class="back__field"></div>
    <p class="back__message">Proud to help people and small businesses file for bankruptcy protection.<br>We are a debt relief agency</p>
    <svg class="back__seal" width="258" height="258" viewBox="0 0 258 258">
      <circle cx="129" cy="129" r="126" fill="var(--paper)"/>
      <circle cx="129" cy="129" r="118" fill="var(--brown)"/>
      <circle cx="129" cy="129" r="90" fill="var(--forest)"/>
      <text class="seal-name" x="129" y="137" text-anchor="middle" font-size="24">M.K. Quentby</text>
    </svg>
  </section>

</body>
</html>
```